A website for Varnholt Limited

We need a new and modern website for our company. We are engineering consultants and contractors (EPC) in the oil and gas industry and building services industry.
What we do:
Engineering, procurement, construction
Automation (safety and process)
Non-destructive testing
Training
We have an existing website and the content can be referred from there since we are remaking the website
For more information visit Varnholt Limited Kenya

Coding

Number of Pages Required

1 page

```html
<!DOCTYPE html>
<html lang="en">
<head>
<meta charset="utf-8">
<title>Varnholt Limited — Engineering, Procurement, Construction</title>
<link rel="stylesheet" href="https://fonts.googleapis.com/css2?family=Open+Sans:ital,wght@0,400;0,600;0,700;0,800;1,400&display=swap">
<style>
:root{
  --navy:#0c1f44;
  --navy-2:#13295a;
  --red:#e31e25;
  --teal:#3cbac8;
  --light:#eef1f5;
  --line:#d9dee6;
  --text:#4d5868;
  --muted:#8b95a3;
  --white:#ffffff;
}
*{box-sizing:border-box;margin:0;padding:0}
html,body{width:1200px;height:3800px;overflow:hidden}
body{position:relative;font-family:"Open Sans",Arial,sans-serif;color:var(--text);background:var(--white);font-size:10px}
.abs{position:absolute}
.topbar{left:0;top:0;width:1200px;height:24px;background:var(--navy);color:#fff;font-size:9px}
.topbar .tag{left:243px;top:6px;font-style:italic}
.topbar .links{left:713px;top:5px;display:flex;gap:14px}
.topbar .dots{left:879px;top:7px;display:flex;gap:11px}
.dot{width:9px;height:9px;border-radius:50%;background:#fff;opacity:.85}
.header{left:0;top:24px;width:1200px;height:94px;background:#fff}
.brand{left:243px;top:40px;display:flex;align-items:center;gap:10px}
.brand .mark{width:34px;height:34px;border-radius:50%;background:var(--red)}
.brand .name{font-size:20px;font-weight:700;color:var(--navy);line-height:1;letter-spacing:1px}
.contact-item{top:44px;display:flex;gap:10px;font-size:9px;color:var(--muted)}
.contact-item b{display:block;color:var(--navy);font-weight:600;margin-top:4px}
.quote-btn{left:861px;top:41px;width:96px;height:31px;background:var(--red);color:#fff;font-weight:700;font-size:9px;display:flex;align-items:center;justify-content:center;letter-spacing:.5px}
.nav{left:243px;top:100px;width:714px;height:30px;background:#fff;border-top:1px solid var(--line);z-index:2;display:flex;align-items:center;padding-left:10px;gap:22px;font-size:8px;font-weight:700;color:var(--navy)}
.nav span::after{content:" ▾";font-size:7px}
.nav .search{position:absolute;right:10px;top:8px}
.hero{left:0;top:118px;width:1200px;height:575px;background:linear-gradient(180deg,#232a6a 0%,#3a3f86 35%,#57507a 60%,#2a2c44 100%)}
.hero h1{left:243px;top:196px;font-size:26px;font-weight:700;color:#fff;line-height:34px;width:330px}
.hero p{left:243px;top:278px;font-size:12px;color:#fff;width:340px;line-height:18px}
.btn{height:28px;color:#fff;font-size:8px;font-weight:700;display:flex;align-items:center;justify-content:center;letter-spacing:.4px}
.arrow-box{width:22px;height:22px;border:1.5px solid #fff;color:#fff;display:flex;align-items:center;justify-content:center;font-size:12px}
.features{left:233px;top:613px;width:732px;height:183px;background:#fff;display:flex;gap:18px;padding:13px 10px}
.feature{flex:1;background:var(--light);border:1px solid var(--line);padding:24px 20px}
.feature h3{font-size:11px;font-weight:700;color:var(--navy);margin:16px 0 10px;letter-spacing:.3px}
.feature p{font-size:9px;line-height:15px}
.sec-head{left:243px;width:714px;border-top:1px solid var(--line)}
.sec-head::before{content:"";position:absolute;left:0;top:-2px;width:157px;height:3px;background:var(--red)}
.sec-head h2{font-size:17px;font-weight:800;color:var(--navy);margin-top:14px;letter-spacing:-.3px}
.sec-head.dark{border-top-color:#3a4a70}
.sec-head.dark h2{color:#fff}
.commit{left:243px;top:893px;width:280px;font-size:20px;font-weight:700;color:var(--navy);line-height:29px;letter-spacing:.4px}
.about-lead{left:548px;top:893px;width:405px;font-size:12px;line-height:18px;color:#3e4d6d}
.about-body{left:548px;top:959px;width:405px;font-size:9px;line-height:15px}
.team{left:0;top:1095px;width:1200px;height:470px;background:var(--light)}
.frame{left:243px;top:1220px;width:254px;height:257px;background:var(--navy)}
.frame-inner{left:265px;top:1245px;width:208px;height:232px;background:#fff}
.person{left:270px;top:1143px;width:230px;height:334px;background:linear-gradient(180deg,#c9ced6 0%,#2a2f3c 55%,#1c2028 100%);border-radius:60px 60px 0 0}
.role-tag{left:243px;top:1452px;width:123px;height:25px;background:var(--teal);color:#fff;font-size:8px;display:flex;align-items:center;padding-left:18px}
.lead-name{left:548px;top:1154px;font-size:18px;color:var(--navy)}
.lead-role{left:548px;top:1178px;font-size:8px;font-weight:700;color:var(--navy)}
.lead-bio{left:548px;top:1210px;width:405px;font-size:9px;line-height:15px}
.quote{left:548px;top:1378px;width:407px;height:70px;background:#fff;border-left:3px solid var(--teal);padding:12px 14px;font-size:9.5px;font-style:italic;line-height:16px;color:var(--muted)}
.projects{left:0;top:1565px;width:1200px;height:771px;background:linear-gradient(135deg,#0e2249 0%,#1a2f5e 60%,#132650 100%)}
.filters{left:251px;top:1703px;display:flex;gap:12px;font-size:8px;font-weight:700;color:#fff}
.filters .on{color:var(--red)}
.proj{width:225px;height:158px}
.testi{left:0;top:2336px;width:1200px;height:358px;background:var(--light)}
.face-box{width:159px;height:159px}
.t-name{font-size:10px;font-weight:700;color:var(--navy)}
.t-co{font-size:8.5px;color:var(--muted);margin-top:5px}
.t-text{font-size:9px;line-height:15px;margin-top:14px;width:170px}
.arrow-dark{width:23px;height:23px;border:1.5px solid var(--navy);color:var(--navy);display:flex;align-items:center;justify-content:center;font-size:12px;background:#fff}
.cta{left:0;top:2694px;width:1200px;height:213px;background:linear-gradient(135deg,#13285a,#1d3567 55%,#132650);text-align:center;color:#fff}
.cta h2{position:absolute;left:0;width:1200px;top:57px;font-size:16px;font-weight:700}
.cta p{position:absolute;left:390px;width:420px;top:90px;font-size:9px;line-height:15px}
.news{width:165px}
.news .img{height:101px}
.news h4{font-size:9.5px;font-weight:700;color:var(--navy);line-height:15px;margin-top:15px}
.news .meta{font-size:8px;color:var(--muted);margin-top:6px;display:flex;gap:14px;padding-bottom:12px;border-bottom:1px solid var(--line)}
.meta i{display:inline-block;width:7px;height:7px;border:1px solid var(--teal);border-radius:50%;margin-right:3px;vertical-align:-1px}
.partner{top:3290px;width:160px;text-align:center;font-size:19px;font-weight:700;color:#3a3a3a;letter-spacing:1px}
.footer{left:0;top:3405px;width:1200px;height:395px;background:var(--navy);color:#fff}
.contact-panel{left:233px;top:3376px;width:732px;height:106px;background:#fff;display:flex;gap:18px;padding:0 10px}
.cbox{flex:1;background:var(--light);border:1px solid var(--line);margin-top:4px;height:91px;text-align:center;padding-top:20px}
.cbox h4{font-size:10.5px;font-weight:700;color:var(--navy);margin-bottom:14px}
.cbox p{font-size:8.5px;line-height:15px}
.fcol{top:3547px;width:170px;font-size:9px;line-height:14px}
.fcol h3{font-size:14px;font-weight:700;margin-bottom:30px;position:relative}
.fcol h3::before{content:"";position:absolute;left:0;top:-14px;width:94px;height:2px;background:#4a3f7a}
.fcol .date{font-size:7.5px;opacity:.8;margin:8px 0 18px}
.fcol .svc{color:var(--teal);margin-bottom:9px;display:block}
.ring{width:22px;height:22px;border-radius:50%;background:#1d3263;display:inline-block;margin-right:5px}
</style>
</head>
<body>

<div class="abs topbar">
  <div class="abs tag">We help the world growing since 1983</div>
  <div class="abs links"><span>Career</span><span>Give Feedback</span><span>Contact Us</span></div>
  <div class="abs dots"><span class="dot"></span><span class="dot"></span><span class="dot"></span><span class="dot"></span></div>
</div>

<div class="abs header"></div>
<div class="abs brand"><span class="mark"></span><span class="name">Varnholt<br>Limited</span></div>
<div class="abs contact-item" style="left:597px">
  <svg width="24" height="18" viewBox="0 0 24 18"><rect x="1" y="1" width="22" height="16" rx="2" fill="none" stroke="#3cbac8" stroke-width="1.6"/><path d="M1 2l11 8 11-8" fill="none" stroke="#3cbac8" stroke-width="1.6"/></svg>
  <div>Email Support<b>info@varnholt.co</b></div>
</div>
<div class="abs contact-item" style="left:729px">
  <svg width="20" height="20" viewBox="0 0 20 20"><path d="M4 2l4 1 1 4-2 2c1 2 3 4 5 5l2-2 4 1 1 4-2 2C9 19 1 11 2 4z" fill="none" stroke="#3cbac8" stroke-width="1.6"/></svg>
  <div>Call Support<b>+254 700 555 118</b></div>
</div>
<div class="abs quote-btn">GET A QUOTE</div>

<div class="abs hero" role="img" aria-label="Photo of an oil refinery lit up at dusk"></div>
<div class="abs nav">
  <span>HOME</span><span>ABOUT US</span><span>SERVICES</span><span>PAGES</span><span>PROJECTS</span><span>NEWS</span><span>CONTACT</span>
  <svg class="search" width="12" height="12" viewBox="0 0 12 12"><circle cx="5" cy="5" r="3.8" fill="none" stroke="#0c1f44" stroke-width="1.5"/><path d="M8 8l3 3" stroke="#0c1f44" stroke-width="1.6"/></svg>
</div>
<h1 class="abs hero" style="height:auto;background:none;top:196px;left:243px;width:330px;font-size:26px;font-weight:700;color:#fff;line-height:34px">Providing Innovative Solution</h1>
<p class="abs" style="left:243px;top:278px;width:340px;font-size:12px;color:#fff;line-height:18px">Lorem ipsum dolor sit amet, consectetur adipisicing elit, sed do eiusmod</p>
<div class="abs btn" style="left:243px;top:348px;width:100px;background:var(--red)">LEARN MORE</div>
<div class="abs btn" style="left:348px;top:348px;width:107px;background:var(--navy)">CONTACT US</div>
<div class="abs arrow-box" style="left:202px;top:432px">‹</div>
<div class="abs arrow-box" style="left:976px;top:432px">›</div>

<div class="abs features">
  <div class="feature">
    <svg width="22" height="22" viewBox="0 0 22 22"><path d="M11 2l2.7 6 6.3.6-4.8 4.2 1.4 6.4L11 16l-5.6 3.2 1.4-6.4L2 8.6 8.3 8z" fill="none" stroke="#8b95a3" stroke-width="1.3"/></svg>
    <h3>QUALITY DRIVEN</h3>
    <p>Lorem ipsum dolor sit amet, consectetur adipisicing elit sed do eiusmod tempor.</p>
  </div>
  <div class="feature">
    <svg width="22" height="22" viewBox="0 0 22 22"><path d="M2 11a9 8 0 0 1 18 0z" fill="#8b95a3"/><path d="M11 11v7a2 2 0 0 1-4 0" fill="none" stroke="#8b95a3" stroke-width="1.5"/></svg>
    <h3>CUSTOMER FOCUSED</h3>
    <p>Lorem ipsum dolor sit amet, consectetur adipisicing elit sed do eiusmod tempor.</p>
  </div>
  <div class="feature">
    <svg width="24" height="22" viewBox="0 0 24 22"><circle cx="6" cy="6" r="3" fill="#8b95a3"/><circle cx="17" cy="6" r="3" fill="#8b95a3"/><circle cx="11.5" cy="9" r="3.5" fill="#8b95a3"/><path d="M1 16a5 5 0 0 1 10 0zM13 16a5 5 0 0 1 10 0zM5 20a6.5 6 0 0 1 13 0z" fill="#8b95a3"/></svg>
    <h3>GLOBAL SOURCING</h3>
    <p>Lorem ipsum dolor sit amet, consectetur adipisicing elit sed do eiusmod tempor.</p>
  </div>
</div>

<div class="abs sec-head" style="top:814px"><h2>ABOUT US</h2></div>
<div class="abs commit">OUR REAL COMMITMENT REACHES BEYOND GAS &amp; OIL COMPANY.</div>
<p class="abs about-lead">Lorem ipsum dolor sit amet, consectetur adipisicing elit, sed do eiusmod tempor incididunt ut labore et dolore magna aliqua. Ut enim ad minim veniam.</p>
<p class="abs about-body">Lorem ipsum dolor sit amet, consectetur adipisicing elit, sed do eiusmod tempor incididunt ut labore et dolore magna aliqua. Ut enim ad minim veniam, quis nostrud exercitation ullamco laboris nisi ut aliquip ex ea commodo consequat. Duis aute irure dolor in reprehenderit in voluptate velit esse cillum dolore eu fugiat nulla pariatur. Excepteur sint occaecat cupidatat non proident, sunt in culpa qui officia deserunt mollit anim id est laborum.</p>

<div class="abs team"></div>
<div class="abs frame"></div>
<div class="abs frame-inner"></div>
<div class="abs person" role="img" aria-label="Portrait of the head of operations in a dark suit"></div>
<div class="abs role-tag">HEAD OF OPERATIONS</div>
<div class="abs lead-name">Daniel Orwa</div>
<div class="abs lead-role">HEAD OF OPERATIONS</div>
<div class="abs lead-bio">
  <p>Lorem ipsum dolor sit amet, consectetur adipisicing elit, sed do eiusmod tempor incididunt ut labore et dolore magna aliqua. Ut enim ad minim veniam, quis nostrud exercitation ullamco laboris nisi ut aliquip ex ea commodo consequat. Duis aute irure dolor in reprehenderit in voluptate velit esse cillum dolore eu fugiat nulla pariatur. Excepteur sint occaecat cupidatat non proident, sunt in culpa qui officia deserunt mollit anim id est laborum.</p>
  <p style="margin-top:12px">Duis aute irure dolor in reprehenderit in voluptate velit esse cillum dolore eu fugiat nulla pariatur. Excepteur sint occaecat cupidatat non proident, sunt in culpa qui officia deserunt mollit anim id est laborum.</p>
</div>
<div class="abs quote">Varnholt Engineering continues to grow ever day thanks to the confidence our clients have in us. We cover many industries such as oil gas, energy, business services, consumer products.</div>

<div class="abs projects"></div>
<div class="abs sec-head dark" style="top:1623px"><h2>PROJECTS</h2></div>
<div class="abs filters"><span class="on">ALL</span><span>ECO</span><span>MANUFACTURING</span><span>INDUSTRY</span><span>OIL</span><span>GAS</span><span>FACTORY</span></div>
<div class="abs proj" style="left:243px;top:1739px;background:linear-gradient(180deg,#3b4fa8,#6d6f9a 55%,#3a3320)" role="img" aria-label="Refinery at night"></div>
<div class="abs proj" style="left:487px;top:1739px;background:linear-gradient(180deg,#dfe8f0,#8c98a6)" role="img" aria-label="Grain silos"></div>
<div class="abs proj" style="left:731px;top:1739px;background:linear-gradient(180deg,#1b4f8c,#5c8fc4 60%,#8fb5db)" role="img" aria-label="Empty warehouse hall"></div>
<div class="abs proj" style="left:243px;top:1916px;background:linear-gradient(135deg,#2e6fb0,#b7c8d8 55%,#5e7f9e)" role="img" aria-label="Industrial pipework"></div>
<div class="abs proj" style="left:487px;top:1916px;background:linear-gradient(135deg,#1d6fb8,#4b8fcf 50%,#1a3f6e)" role="img" aria-label="Solar panel array"></div>
<div class="abs proj" style="left:731px;top:1916px;background:linear-gradient(90deg,#0f3560,#5f97c9 55%,#1d4e7d)" role="img" aria-label="Factory interior with shutters"></div>
<div class="abs proj" style="left:243px;top:2093px;background:linear-gradient(180deg,#4a5a8f,#7d6f8c 45%,#1b2242)" role="img" aria-label="Power plant at dusk"></div>
<div class="abs proj" style="left:487px;top:2093px;background:linear-gradient(180deg,#3a9ad4,#6e8a7a 60%,#3d4a36)" role="img" aria-label="Old industrial plant under blue sky"></div>
<div class="abs proj" style="left:731px;top:2093px;background:linear-gradient(180deg,#14213d,#5a5d78 55%,#c06a3a 75%,#1a1d2c)" role="img" aria-label="Wind turbines at sunset"></div>

<div class="abs testi"></div>
<div class="abs sec-head" style="top:2405px"><h2>TESTIMONIALS</h2></div>
<div class="abs arrow-dark" style="left:203px;top:2536px">‹</div>
<div class="abs arrow-dark" style="left:972px;top:2536px">›</div>
<div class="abs face-box" style="left:243px;top:2478px;background:linear-gradient(135deg,#5b5246,#a89d8e 55%,#1c1c1c)" role="img" aria-label="Portrait of a client"></div>
<div class="abs" style="left:422px;top:2481px">
  <div class="t-name">Martin Kessler</div><div class="t-co">Rift Gas Ltd</div>
  <p class="t-text">Lorem Ipsum is simply dummy text of the printing and typesetting industry orem Ipsum has been. Mauris ornare tortor in eleifend blanditullam ut ligula et neque. Nulla interdum dapibus erat nec elementum.</p>
</div>
<div class="abs face-box" style="left:609px;top:2478px;background:linear-gradient(135deg,#8a7a68,#c2ab92 55%,#5e4a3a)" role="img" aria-label="Portrait of a client"></div>
<div class="abs" style="left:787px;top:2481px">
  <div class="t-name">Amina Wekesa</div><div class="t-co">Lakeway Ltd</div>
  <p class="t-text">Lorem Ipsum is simply dummy text of the printing and typesetting industry orem Ipsum has been. Mauris ornare tortor in eleifend blanditullam ut ligula et neque. Nulla interdum dapibus erat nec elementum.</p>
</div>

<div class="abs cta">
  <h2>If you need industrial solution... We are available for you</h2>
  <p>We provide innovative solutions for sustainable progress. Our professional team works to increase productivity and cost effectiveness on the market</p>
  <div class="abs btn" style="left:554px;top:133px;width:92px;height:28px;background:var(--red)">CONTACT US</div>
</div>

<div class="abs sec-head" style="top:2963px"><h2>RECENT NEWS</h2></div>
<div class="abs news" style="left:243px;top:3036px">
  <div class="img" style="background:linear-gradient(180deg,#d9dfe3,#c89a3c 55%,#6a5a3e)" role="img" aria-label="Workers at a drilling rig"></div>
  <h4>The Best in dolor sit amet consectetur adipisicing elit sed</h4>
  <div class="meta"><span><i></i>Aug 24, 2017</span><span><i></i>0 Comments</span></div>
</div>
<div class="abs news" style="left:426px;top:3036px">
  <div class="img" style="background:linear-gradient(135deg,#1e4a9a,#c8cfd8 60%,#4a5360)" role="img" aria-label="Engineer holding a hard hat"></div>
  <h4>The Best in dolor sit amet consectetur adipisicing elit sed</h4>
  <div class="meta"><span><i></i>Aug 24, 2017</span><span><i></i>0 Comments</span></div>
</div>
<div class="abs news" style="left:609px;top:3036px">
  <div class="img" style="background:linear-gradient(135deg,#d8a93a,#5a7fb0 55%,#2c3e5c)" role="img" aria-label="Technician working on machinery"></div>
  <h4>The Best in dolor sit amet consectetur adipisicing elit sed</h4>
  <div class="meta"><span><i></i>Aug 24, 2017</span><span><i></i>0 Comments</span></div>
</div>
<div class="abs news" style="left:792px;top:3036px">
  <div class="img" style="background:linear-gradient(135deg,#b7c23a,#8c98a6 55%,#d9dee6)" role="img" aria-label="Two engineers in safety vests"></div>
  <h4>The Best in dolor sit amet consectetur adipisicing elit sed</h4>
  <div class="meta"><span><i></i>Aug 24, 2017</span><span><i></i>0 Comments</span></div>
</div>

<div class="abs partner" style="left:238px">KESTREL</div>
<div class="abs partner" style="left:428px">FIELDLINE</div>
<div class="abs partner" style="left:612px">BRIGHTWASH</div>
<div class="abs partner" style="left:794px">TONEHALL</div>

<div class="abs footer"></div>
<div class="abs contact-panel">
  <div class="cbox"><h4>CALL US NOW</h4><p>Office Telephone: +254 700 555 120<br>Mobile: +254 700 555 121</p></div>
  <div class="cbox"><h4>COME VISIT US</h4><p>14 Mombasa Road, Nairobi 00100,<br>Kenya</p></div>
  <div class="cbox"><h4>SEND US A MESSAGE</h4><p>General: info@varnholt.co<br>Sales: sales@varnholt.co</p></div>
</div>

<div class="abs brand" style="top:3540px"><span class="mark"></span><span class="name" style="color:#fff">Varnholt<br>Limited</span></div>
<p class="abs" style="left:243px;top:3600px;width:165px;font-size:9px;line-height:14px;color:#fff">This template is a micro niche for business categories, namely Varnholt - Industrial HTML Template. there was an excess of this template is using HTML/CSS.</p>
<div class="abs" style="left:243px;top:3700px"><span class="ring"></span><span class="ring"></span><span class="ring"></span><span class="ring"></span></div>

<div class="abs fcol" style="left:426px">
  <h3>Recent Post</h3>
  <p>The Best in dolor sit amet consectetur adipisicing elit sed</p><p class="date">◷ June 16, 2017</p>
  <p>The Best in dolor sit amet consectetur adipisicing elit sed</p><p class="date">◷ June 16, 2017</p>
</div>
<div class="abs fcol" style="left:609px">
  <h3>Our Services</h3>
  <span class="svc">Mechanical Engineering</span><span class="svc">Agricultural Processing</span><span class="svc">Oil and Lubricants</span><span class="svc">Power and Energy</span><span class="svc">Chemical Research</span><span class="svc">Material Engineering</span>
</div>
<div class="abs fcol" style="left:792px">
  <h3>Subscribe</h3>
  <p>Lit sed The Best in dolor sit amet consectetur adipisicing elit sedconsectetur adipisicing</p>
  <div style="display:flex;margin-top:16px;height:22px"><div style="width:140px;background:#fff;color:#999;font-size:8px;padding:5px 10px">enter your email</div><div style="width:24px;background:var(--red);display:flex;align-items:center;justify-content:center"><svg width="10" height="8" viewBox="0 0 10 8"><rect x=".5" y=".5" width="9" height="7" fill="none" stroke="#fff"/><path d="M.5 .5l4.5 4 4.5-4" fill="none" stroke="#fff"/></svg></div></div>
  <p style="font-size:8px;margin-top:10px">Get latest updates and offers.</p>
</div>

</body>
</html>
```